Business card for new business.
Red and black corporate colors.
Card can have an Indsutrial feel to it. Feel free to add Rust, Bolted steel, or graphics as you see fit. We provide highly specialized services to the below mentioned industries.
Keep information out of corners so that if I want I can choose rounded corners.
Information
- front. name - title - phone - email
- Rear
Refining - Rail - Infrastructure - Mining - Energy
Northgate - Ashford - Pine Hollow - Stonebridge - Harbourview

```html
<!DOCTYPE html>
<html lang="en">
<head>
<meta charset="utf-8">
<title>Ironward — Business Card</title>
<link rel="stylesheet" href="https://fonts.googleapis.com/css2?family=Archivo:wght@400;800&display=swap">
<style>
  :root {
    --backdrop: #2b2b2d;
    --card: #050505;
    --red: #e2232a;
    --grey: #8f8f8f;
    --light: #c9c9c9;
  }
  * { margin: 0; padding: 0; box-sizing: border-box; }
  html, body {
    width: 1200px; height: 880px; overflow: hidden;
    background: var(--backdrop);
    font-family: "Archivo", Arial, sans-serif;
  }
  .stage {
    width: 1200px; height: 880px;
    display: flex; flex-direction: column;
    align-items: center; justify-content: center; gap: 30px;
  }
  .card {
    width: 700px; height: 400px;
    background: var(--card);
    border-radius: 22px;
    position: relative;
    box-shadow: 0 14px 40px rgba(0,0,0,.55);
  }
  .brand {
    display: flex; align-items: center; gap: 14px; flex: none;
  }
  .brand-square {
    width: 30px; height: 30px; background: var(--red); flex: none;
  }
  .brand-name {
    font-weight: 800; letter-spacing: 2px; color: var(--light); white-space: nowrap;
  }

  /* Rear */
  .card-rear {
    display: flex; flex-direction: column; align-items: center; justify-content: center;
  }
  .card-rear .brand-name { font-size: 60px; color: #9a9a9a; }
  .card-rear .brand-square { background: #5a5a5a; }
  .rear-lists { margin-top: 70px; text-align: center; }
  .rear-line { font-size: 17px; color: var(--grey); line-height: 1.5; white-space: nowrap; }
  .sep { color: var(--red); padding: 0 6px; }

  /* Front */
  .card-front {
    display: flex; align-items: center; padding: 0 50px 0 70px;
  }
  .card-front .brand { transform: translateY(40px); }
  .card-front .brand-name { font-size: 44px; }
  .divider {
    flex: none;
    width: 2px; height: 110px; background: var(--red);
    margin: 0 30px 0 34px; transform: translateY(-40px);
  }
  .contact { transform: translateY(-40px); white-space: nowrap; }
  .person-name { color: var(--red); font-size: 20px; letter-spacing: .5px; }
  .person-title { color: var(--light); font-size: 15px; margin-bottom: 14px; }
  .contact-row {
    display: flex; align-items: center; gap: 8px;
    color: var(--light); font-size: 15px; line-height: 1.6;
  }
  .contact-row svg { width: 13px; height: 13px; fill: var(--red); flex: none; }
</style>
</head>
<body>
<main class="stage">
  <section class="card card-rear">
    <div class="brand">
      <span class="brand-square"></span>
      <span class="brand-name">IRONWARD</span>
    </div>
    <div class="rear-lists">
      <p class="rear-line">Refining<span class="sep">|</span>Rail<span class="sep">|</span>Infrastructure<span class="sep">|</span>Mining<span class="sep">|</span>Energy</p>
      <p class="rear-line">Northgate<span class="sep">|</span>Ashford<span class="sep">|</span>Pine Hollow<span class="sep">|</span>Stonebridge<span class="sep">|</span>Harbourview</p>
    </div>
  </section>

  <section class="card card-front">
    <div class="brand">
      <span class="brand-square"></span>
      <span class="brand-name">IRONWARD</span>
    </div>
    <span class="divider"></span>
    <div class="contact">
      <p class="person-name">NOAH BENNETT</p>
      <p class="person-title">Managing Director</p>
      <p class="contact-row">
        <svg viewBox="0 0 16 16" aria-hidden="true"><path d="M3.6 1 6 3.4 4.6 5.2c.9 2 2.3 3.4 4.2 4.3l1.8-1.4L13 10.4 11.6 13C6.4 12.8 3.2 9.6 1 4.4z"/></svg>
        (01) 5550 1234
      </p>
      <p class="contact-row">
        <svg viewBox="0 0 16 16" aria-hidden="true"><path d="M1 3h14v10H1zM2 4v.4l6 4.2 6-4.2V4z"/></svg>
        hello@ironwardgroup.com
      </p>
    </div>
  </section>
</main>
</body>
</html>
```